Flyer für Unternehmensberatung für betriebliche Gesundheitsförderung
Zielgruppe
Unternehmensberatung für betriebliche Gesundheitsförderung - wir machen Mitarbeiter gesünder und leistungsfähiger
Aufgabenstellung
Ich lege Textmaterial als Vorlage bei

```html
<!DOCTYPE html>
<html lang="de">
<head>
<meta charset="utf-8">
<title>Unternehmensberatung Tobias Kessler – Broschüre</title>
<link rel="stylesheet" href="https://fonts.googleapis.com/css2?family=Montserrat:wght@600;700;800&family=Open+Sans:wght@400;600;700&display=swap">
<style>
:root{
  --cream:#fdeecb;
  --ink:#0e0e0e;
  --text:#2a2a2a;
  --blue:#3b7ea8;
  --blue-dark:#2f6f98;
  --gold:#f5d98f;
  --paper:#ffffff;
  --stage:#efefef;
}
*{box-sizing:border-box;margin:0;padding:0}
html,body{width:750px;height:1200px;overflow:hidden}
body{background:var(--stage);position:relative;font-family:"Open Sans",Arial,sans-serif;color:var(--text)}
.page{position:absolute;width:420px;height:594px;background:var(--paper);overflow:hidden;transform-origin:0 0;box-shadow:0 1px 4px rgba(0,0,0,.12);font-size:7.2px;line-height:1.55}
.cover{left:225px;top:34px;transform:scale(.7143)}
.p2{left:35px;top:506px;transform:scale(.5)}
.p3{left:270px;top:506px;transform:scale(.5)}
.p4{left:505px;top:506px;transform:scale(.5)}
.p5{left:35px;top:836px;transform:scale(.5)}
.p6{left:270px;top:836px;transform:scale(.5)}

/* cover */
.cover-brand{height:140px;background:var(--cream);display:flex;align-items:center;justify-content:center}
.brand-name{font-family:"Montserrat",sans-serif;font-weight:700;font-size:28px;color:var(--ink)}
.cover-photo{height:290px;background:linear-gradient(180deg,#e9e4dc 0%,#d9c9a8 45%,#b58a6e 75%,#8c7b70 100%)}
.cover-title{height:164px;background:var(--ink);text-align:center;padding-top:28px;font-family:"Montserrat",sans-serif}
.cover-title h1{color:var(--gold);font-weight:800;font-size:20px;line-height:1.35;letter-spacing:.6px}
.cover-title h2{color:#fff;font-weight:700;font-size:14px;margin-top:6px}
.cover-pill{display:inline-block;background:var(--blue);color:#fff;font-family:"Open Sans",sans-serif;font-weight:600;font-size:10px;padding:3px 9px;margin-top:8px}

/* running header */
.runhead{position:absolute;top:28px;display:flex;align-items:center;gap:4px;font-size:6px;color:#333}
.runhead b{color:var(--blue);font-weight:600}
.runhead .tab{background:var(--blue);color:#fff;width:36px;height:8px;font-size:5.5px;padding-left:5px;line-height:8px}
.runhead.right{right:0}
.runhead.left{left:0}
.on-dark{color:#ddd}

.sec{padding:0 40px 0 48px}
.h{font-family:"Montserrat",sans-serif;font-weight:700;font-size:8px;color:var(--ink);margin:0 0 5px -10px;display:flex;align-items:center;gap:5px}
.h::before{content:"";flex:none;width:4px;height:4px;background:currentColor}
.dark .h{color:#fff}
ul.dots{list-style:none}
ul.dots li{position:relative;padding-left:12px}
ul.dots li::before{content:"";position:absolute;left:2px;top:4px;width:3px;height:3px;border-radius:50%;background:var(--blue)}
ul.ticks{list-style:none}
ul.ticks li{position:relative;padding-left:12px}
ul.ticks li::before{content:"";position:absolute;left:0;top:2px;width:6px;height:6px;border:1px solid var(--blue)}
ul.ticks li::after{content:"";position:absolute;left:2px;top:2.5px;width:2px;height:3.5px;border:solid var(--blue);border-width:0 1px 1px 0;transform:rotate(45deg)}
.dark{background:var(--ink);color:#e6e6e6}
.price{font-family:"Montserrat",sans-serif;font-weight:700;color:var(--blue-dark);font-size:8.5px}
.label{font-weight:700;color:var(--ink)}
.box{background:var(--cream);padding:12px 14px}
.blk{margin-top:10px}

/* page 2 */
.p2 .top{padding-top:70px}
.p2 .howto{position:absolute;left:0;right:0;top:358px;bottom:0;padding-top:22px}
.icons{display:grid;grid-template-columns:1fr 1fr;gap:12px 10px;margin:6px 0 18px}
.icon-item{display:flex;gap:8px;align-items:flex-start}
.icon-item svg{flex:none}
.criteria{display:flex;gap:16px;margin-top:6px}

/* page 3 */
.p3 .hero{position:absolute;inset:0 0 190px 0}
.portrait{position:absolute;left:0;top:58px;width:200px;height:300px;background:radial-gradient(ellipse at 50% 35%,#3a342e 0%,#1c1a18 55%,var(--ink) 100%)}
.portrait-cap{position:absolute;left:48px;top:338px;color:#fff;font-size:6.5px}
.portrait-cap strong{font-family:"Montserrat",sans-serif;font-size:9px;display:block}
.steps{position:absolute;left:185px;top:74px;right:36px}
.step{display:grid;grid-template-columns:16px 1fr;margin-bottom:10px}
.step b{color:#fff;font-weight:700}
.p3 .bottom{position:absolute;top:420px;left:0;right:0}

/* page 4 */
.p4 .cols{position:absolute;top:72px;left:36px;right:22px;display:grid;grid-template-columns:1fr 180px;gap:12px}
.p4 .cta{position:absolute;left:0;right:0;bottom:0;height:192px;padding:44px 0 0 48px}
.cta h3{font-family:"Montserrat",sans-serif;font-weight:700;font-size:8px;color:var(--blue);margin-bottom:8px}
.contact{list-style:none;margin-top:14px}
.contact li{display:flex;align-items:center;gap:7px;margin-bottom:2px}
.cta-photo{position:absolute;right:40px;bottom:0;width:150px;height:176px;background:radial-gradient(ellipse at 50% 40%,#3d3833 0%,#1f1d1b 60%,var(--ink) 100%)}

/* page 5 */
.p5 .hero{position:absolute;left:0;right:0;top:0;height:282px;background:linear-gradient(135deg,#2a3340 0%,#3b4656 40%,#1d2530 75%,#11161c 100%)}
.p5 .hero-text{position:absolute;left:48px;right:36px;top:178px;color:#ddd}
.p5 .hero-text .h{color:#fff}
.p5 .body{position:absolute;top:300px;left:0;right:0}

/* page 6 */
.p6 .content{position:absolute;top:72px;left:0;right:0}
.num{display:grid;grid-template-columns:32px 1fr;margin-bottom:6px}
.num span{font-family:"Montserrat",sans-serif;font-size:14px;font-weight:600;color:var(--blue);line-height:1}
.p6 .invest{display:grid;grid-template-columns:1fr 150px;gap:10px;padding-right:26px}
.p6 .footer{position:absolute;left:0;right:0;bottom:0;height:34px;display:flex;justify-content:space-around;align-items:center;font-size:6.5px}
.p6 .footer span{display:flex;align-items:center;gap:5px}
.p6 .kontakt{position:absolute;right:0;bottom:34px;background:var(--blue);color:#fff;font-weight:700;font-size:6.5px;padding:3px 20px}
</style>
</head>
<body>

<section class="page cover">
  <div class="cover-brand">
    <div class="brand-name">Tobias Kessler</div>
  </div>
  <div class="cover-photo" role="img" aria-label="Foto: jubelndes Team mit erhobenen Armen in hellem Büro"></div>
  <div class="cover-title">
    <h1>UNTERNEHMENSBERATUNG<br>TOBIAS KESSLER, MBA</h1>
    <h2>Gesunde Mitarbeitende. Starke Unternehmen.</h2>
    <div class="cover-pill">Mit dem MEA Score zu messbarem Unternehmenserfolg</div>
  </div>
</section>

<section class="page p2">
  <div class="runhead right"><b>Unternehmensberatung</b> | Tobias Kessler, MBA <span class="tab">2</span></div>
  <div class="top sec">
    <div class="h">Zielsetzung: Gesundheit trifft Produktivität</div>
    <p>Unser Ziel ist die Symbiose aus gesunden, motivierten Mitarbeitenden und messbar besseren Unternehmensergebnissen. Mit unserem weltweit einzigartigen Programm reduzieren Sie nicht nur in erheblichem Ausmaß Fehlzeiten, sondern steigern nachhaltig die Leistungsfähigkeit Ihrer Teams.</p>
    <div class="h" style="margin-top:14px">Ergebnisse auf einen Blick:</div>
    <ul class="dots">
      <li>Deutliche Reduktion von Erschöpfung und Lebensstilbedingter Müdigkeit</li>
      <li>Stark spürbarer Rückgang von Absentismus am Arbeitsplatz (wie beispielsweise durch Krankenstand)</li>
      <li>Prävention von Burnout &amp; Depressionen</li>
      <li>Langfristige Bindung von Leistungsträgern</li>
      <li>Weniger Fluktuation = geringere Kosten für Wiedereinstellung &amp; Einschulung</li>
      <li>Positionierung als attraktiver Arbeitgeber im „War for Talents“</li>
    </ul>
    <div class="h" style="margin-top:14px">Der MEA Score – Ihr Benchmark für Unternehmenserfolg</div>
    <p>Der <b>MutEnergieAmbition Score</b> (MEA Score) ist ein innovatives Messsystem, das den Zusammenhang zwischen Gesundheit, Motivation und Unternehmenserfolg sichtbar macht.</p>
  </div>
  <div class="howto dark sec">
    <div class="h">So funktioniert es:</div>
    <div class="icons">
      <div class="icon-item"><svg width="16" height="16" viewBox="0 0 16 16" fill="none" stroke="#ddd" stroke-width="1"><rect x="3" y="2" width="10" height="12"/><path d="M5 6h6M5 9h6M5 12h4"/></svg><span>Erhebung von Gesundheits- &amp; Leistungsdaten zum Programmstart</span></div>
      <div class="icon-item"><svg width="16" height="16" viewBox="0 0 16 16" fill="none" stroke="#ddd" stroke-width="1"><circle cx="7" cy="7" r="5"/><path d="M11 11l4 4M5 8l2-2 2 2"/></svg><span>Auswertung anhand vorhandener Absentismus- &amp; Kostenstellenkennzahlen</span></div>
      <div class="icon-item"><svg width="16" height="16" viewBox="0 0 16 16" fill="none" stroke="#ddd" stroke-width="1"><rect x="3" y="2" width="10" height="12"/><path d="M5 10l2 2 4-5"/></svg><span>Ursachenanalyse: Ernährung, Fitness, Schlafqualität, Resilienz &amp; Stressmanagement</span></div>
      <div class="icon-item"><svg width="16" height="16" viewBox="0 0 16 16" fill="none" stroke="#ddd" stroke-width="1"><circle cx="8" cy="8" r="6"/><circle cx="8" cy="8" r="2.5"/></svg><span>Ableitung konkreter Maßnahmen zur Optimierung</span></div>
    </div>
    <div class="h">Der MEA Score – Ihr Benchmark für Unternehmenserfolg</div>
    <div class="criteria"><span>☑ Messbar</span><span>☑ Nachweisbar</span><span>☑ Reproduzierbar</span></div>
  </div>
</section>

<section class="page p3">
  <div class="hero dark">
    <div class="runhead left on-dark"><span class="tab">3</span><b>Unternehmensberatung</b> | Tobias Kessler, MBA</div>
    <div class="portrait" role="img" aria-label="Porträtfoto des Beraters im dunklen Pullover vor dunklem Hintergrund"></div>
    <div class="portrait-cap"><strong>Tobias Kessler, MBA</strong>Unternehmensberater</div>
    <div class="steps">
      <div class="h" style="margin-left:0">Der Weg zum Erfolg: 3 Schritte</div>
      <div class="step"><b>01</b><div><b>Information – Inspiration – Motivation</b><br>Zu Beginn steht ein emotionaler Impulsvortrag von Tobias Kessler, dessen eigene Heldengeschichte bereits tausende Menschen zu einem gesünderen, leistungsfähigeren Lebensstil inspiriert hat. Die Aufzeichnung steht auch jenen zur Verfügung, die nicht live teilnehmen können.</div></div>
      <div class="step"><b>02</b><div><b>Analyse &amp; Erhebung</b><br>Parallel zur Motivationsphase erfolgt eine umfassende Datenerhebung – die Grundlage für den individuellen MEA Score und den maßgeschneiderten Maßnahmenplan.</div></div>
      <div class="step"><b>03</b><div><b>Umsetzung &amp; Transformation</b><br>Begleitet durch App, Lernplattform und Experten entsteht eine nachhaltige Veränderung im Arbeitsalltag – dokumentiert und sichtbar über die Entwicklung des MEA Scores.</div></div>
    </div>
  </div>
  <div class="bottom sec">
    <div class="h">Ergebnisse auf einen Blick:</div>
    <ul class="dots">
      <li>Wie leistungsfähig sind meine Mitarbeitenden – heute und in Zukunft?</li>
      <li>Welche finanziellen Verluste entstehen durch Fehlzeiten und reduzierte Produktivität?</li>
      <li>Wie viel Potenzial steckt in gesünderen, motivierteren Teams?</li>
      <li>Welche Kosten verursachen unnötige Austritte &amp; Re-Recruiting?</li>
      <li>Was kann ich tun, um diese Verluste in nachhaltige Gewinne zu verwandeln?</li>
      <li>Und zuletzt die wichtigste Frage: Was läuft in meinem Unternehmen nicht optimal, respektive warum ist das ermittelte Einsparungspotential so hoch? Und ja, die Zahlen werden Sie beeindrucken, lassen Sie sich von uns überraschen!</li>
    </ul>
  </div>
</section>

<section class="page p4">
  <div class="runhead right"><b>Unternehmensberatung</b> | Tobias Kessler, MBA <span class="tab">4</span></div>
  <div class="cols">
    <div style="padding-left:12px">
      <div class="h">Leistungen &amp; Investitionen</div>
      <div class="label">Impulsvortrag von Tobias Kessler:</div>
      <div class="price">€ 25.000</div>
      <div>(inkl. Aufzeichnung)</div>
      <div class="label blk">Laufende Programmkosten:</div>
      <div class="price">€ 5,90 / Mitarbeitender / Monat</div>
      <div>(Inklusive exklusiver App &amp; Zugang zur VitaFlix Plattform)</div>
      <div class="label blk">Erfolgsbeteiligung:</div>
      <div>Ein vereinbarter Prozentsatz der jährlichen Einsparung – gemessen an der Verbesserung des MEA Scores.</div>
      <div class="h" style="margin-top:30px">Empfohlene Programmdauer</div>
      <ul class="ticks" style="font-weight:600">
        <li>3 Monate Intensivprogramm</li>
        <li>9–12 Monate für nachhaltige Ergebnisse</li>
      </ul>
    </div>
    <div>
      <div class="box">
        <div class="h" style="margin-left:0">Digitale Begleiter: App &amp; VitaFlix Portal</div>
        <div>Die MEA App – Ihr interaktiver Coach im Alltag:</div>
        <ul class="ticks" style="margin:4px 0 8px">
          <li>Persönliches Lifestyle-Tagebuch</li>
          <li>Tipps, Übungen &amp; Rezepte</li>
          <li>Motivierende „Vitagotchi“-Begleiter</li>
        </ul>
        <div>Das VitaFlix Portal – Wissen, das wirkt:</div>
        <ul class="ticks" style="margin-top:4px">
          <li>Exklusive Lernvideos &amp; Kurse</li>
          <li>Rezepte, Nährstoffe &amp; Einkaufshilfen</li>
          <li>Infotheken für Mitarbeitende &amp; Führungskräfte</li>
        </ul>
      </div>
      <div class="box" style="margin-top:10px">
        <div class="h" style="margin-left:0">Der MEA Score – Ihr Benchmark für Unternehmenserfolg</div>
        <div style="font-weight:600">In 72 Stunden starten – 60 Tage durchhalten – neue Gewohnheit etablieren!</div>
        <div>Denn: Veränderung beginnt mit einer Entscheidung. Nachhaltigkeit entsteht durch Wiederholung.</div>
      </div>
    </div>
  </div>
  <div class="cta dark">
    <h3>Jetzt anfragen &amp; Ihr Unternehmen stärken!</h3>
    <div>Kontaktieren Sie uns für ein<br>unverbindliches Erstgespräch</div>
    <ul class="contact">
      <li><svg width="7" height="7" viewBox="0 0 10 10"><path d="M2 1l2 2-1 1.5a6 6 0 0 0 2.5 2.5L7 6l2 2-1.5 1.5C4 9 1 6 .5 2.5z" fill="var(--blue)"/></svg>tkessler@verbindung.at</li>
      <li><svg width="7" height="7" viewBox="0 0 10 10"><rect x="1" y="2" width="8" height="6" fill="var(--blue)"/></svg>+43-660-5812394</li>
      <li><svg width="7" height="7" viewBox="0 0 10 10" fill="none" stroke="var(--blue)"><circle cx="5" cy="5" r="4"/><path d="M1 5h8M5 1v8"/></svg>www.tobias-kessler.com</li>
    </ul>
    <div class="cta-photo" role="img" aria-label="Porträtfoto des lächelnden Beraters vor dunklem Hintergrund"></div>
  </div>
</section>

<section class="page p5">
  <div class="hero" role="img" aria-label="Foto: zwei lachende Kolleg:innen im Büro vor einem Laptop"></div>
  <div class="runhead left on-dark"><span class="tab">5</span><b>Unternehmensberatung</b> | Tobias Kessler, MBA</div>
  <div class="hero-text">
    <div class="h">Gesunde &amp; leistungsfähige Mitarbeitende<br>für messbare Unternehmenserfolge</div>
    <p>Zielsetzung: Erreichen Sie eine Symbiose aus Gesundheit und Leistungsfähigkeit Ihrer Mitarbeitenden durch den innovativen "MEA Score". Dieses neuartige Benchmark-System ermöglicht eine messbare und reproduzierbare Verbesserung der Unternehmenskennzahlen durch gezielte Gesundheitsförderung.</p>
  </div>
  <div class="body sec">
    <div class="h">Ihre Vorteile auf einen Blick:</div>
    <ul class="dots">
      <li>Reduktion lebensstilbedingter Ermüdungserscheinungen &amp; Erschöpfungssyndrome</li>
      <li>Minimierung von Burnout &amp; Depressionen</li>
      <li>Höhere Bindung der Mitarbeitenden, geringere Fluktuation</li>
      <li>Einsparung von Wiedereinstellungs- &amp; Einschulungskosten</li>
      <li>Vermeidung von Frührente &amp; Krankenständen</li>
      <li>Stärkung Ihrer Arbeitgebermarke im "War for Talents"</li>
    </ul>
    <div class="h" style="margin-top:12px">Zielsetzung: Gesundheit trifft Produktivität</div>
    <p>Ein wissenschaftlich fundiertes System zur Ermittlung gesundheitsbezogener Leistungssteigerungen. Zum Stichtag wird der Gesundheitszustand und die Leistungsfähigkeit Ihrer Mitarbeitenden anhand vorhandener Absentismus-Daten erfasst und mit Unternehmenserfolg und Kostenstellen verknüpft.</p>
    <div class="h" style="margin-top:12px">Typische Ursachen für Leistungsausfälle:</div>
    <ul class="dots">
      <li>Fehlernährung (Makro- &amp; Mikronährstoffmangel)</li>
      <li>Mangelnde Bewegung &amp; Fitness</li>
      <li>Schlechte Schlafqualität</li>
      <li>Geringe Resilienz &amp; hoher Distress</li>
    </ul>
  </div>
</section>

<section class="page p6">
  <div class="runhead right"><b>Unternehmensberatung</b> | Tobias Kessler, MBA <span class="tab">6</span></div>
  <div class="content">
    <div class="sec">
      <div class="h">Zielsetzung: Gesundheit trifft Produktivität</div>
      <div class="num"><span>01</span><div><b>Impulsvortrag von Tobias Kessler:</b> Die "Heldengeschichte" inspiriert Ihre Belegschaft, das eigene Potenzial zu entfalten. Eine Aufzeichnung steht für abwesende Mitarbeitende zur Verfügung.</div></div>
      <div class="num"><span>02</span><div><b>Datenerhebung &amp; Evaluierung:</b> Ermittlung des ersten MEA Scores und sofortiger Start erster Maßnahmen.</div></div>
      <div class="num"><span>03</span><div><b>Umsetzungsphase:</b> Begleitung durch interaktive Tools, Lerninhalte &amp; Gesundheitsangebote.</div></div>
      <div class="h" style="margin-top:10px">Ergebnisse auf einen Blick:</div>
      <ul class="dots">
        <li>Wie leistungsfähig sind meine Mitarbeitenden aktuell?</li>
        <li>Welcher Wertschöpfungsverlust entsteht durch Fehlzeiten?</li>
        <li>Welchen Nutzen bringt mir die Reduktion von Leistungseinbußen?</li>
        <li>Welche (vermeidbaren) Austritts- &amp; Wiedereinstellungskosten habe ich?</li>
        <li>Wie hoch ist mein jährlicher Verlust durch krankheitsbedingte Ausfälle?</li>
      </ul>
      <div class="h" style="margin-top:12px">Investition in Ihre Zukunft:</div>
    </div>
    <div class="invest sec">
      <div>
        <div class="label">Impulsvortrag:</div>
        <div class="price">€ 25.000</div>
        <div class="label blk">App-Nutzung &amp; VitaFlix-Portal:</div>
        <div class="price">€ 5,90 pro Mitarbeiter:in/Monat*</div>
        <div class="label blk">Erfolgsbeteiligung:</div>
        <div>Prozentsatz der jährlichen Einsparung gemessen an MEA Score-Verbesserung</div>
        <div class="blk" style="font-style:italic">*Inklusive Innovations-App mit:</div>
        <ul class="dots">
          <li>Interaktivem Tagebuch für Lebensstil-veränderungen</li>
          <li>Motivation durch "Vitagotchi"</li>
          <li>Tipps, Rezepte, Übungen</li>
          <li>Zugang zu Videos, Kursen, Infotheken u.v.m.</li>
        </ul>
      </div>
      <div class="box" style="align-self:start">
        <div class="h" style="margin-left:0">Dauer &amp; Nachhaltigkeit:</div>
        <ul class="ticks">
          <li>Programme ab 3 Monaten (Intensiv)</li>
          <li>Empfohlen: 9–12 Monate für nachhaltige Wirkung</li>
        </ul>
        <div class="h" style="margin:12px 0 5px">Die goldene MEA 72/60 Regel:</div>
        <div>Starten Sie innerhalb von 72 Stunden nach der Entscheidung und halten Sie 60 Tage durch – dann wird Gesundheit zur Gewohnheit!</div>
      </div>
    </div>
  </div>
  <div class="kontakt">Kontakt: Kessler &amp; Partner KG</div>
  <div class="footer dark">
    <span><svg width="7" height="7" viewBox="0 0 10 10"><path d="M2 1l2 2-1 1.5a6 6 0 0 0 2.5 2.5L7 6l2 2-1.5 1.5C4 9 1 6 .5 2.5z" fill="var(--blue)"/></svg>+43-660-5812394</span>
    <span><svg width="7" height="7" viewBox="0 0 10 10"><rect x="1" y="2" width="8" height="6" fill="var(--blue)"/></svg>tkessler@verbindung.at</span>
    <span><svg width="7" height="7" viewBox="0 0 10 10" fill="none" stroke="var(--blue)"><circle cx="5" cy="5" r="4"/><path d="M1 5h8M5 1v8"/></svg>www.tobias-kessler.com</span>
  </div>
</section>

</body>
</html>
```